Q7 Engineering Rail Sector Brochure

We need a new 3 page folding brochure for Q7 Engineering Pty Ltd. The organisation is currently supporting customers in Defence, Maritime and Information and Communications Technology companies. We are currently looking to expand our engineering services into the rail sector by providing manpower and consultancy services to railway sector clients.We would like the brochure to be based on an A4 page and look technical with particular focus on communications systems used within the railways. This could include pictures of rail control centres, trains (Australian trains only please), train radio communications equipment, radio antennas, computers and networking equipment. Please use both graphics and photos.The brochure will be provided to potential rail customers and should be clear and uncluttered.The following is our company website: www.q7engineering.com.au if you would like more detail on our current work.I have attached the file for our logo which should appear on the brochure.
Target Market(s)
Providing manpower and consultancy services to the railway sector. This includes rail companies (e.g. Harwick Loop Trains, T/Run etc) and rail equipment and carriage suppliers (e.g. Falverine)
Colors
Designer to choose colors to be used in the design.
Requirements
Must have
- Instead of having "lorem ipsum" text in the brochure you can please use some of the text in the file we have provided. Not all has to be used, and you should not be limited to what is in the file.
Nice to have
- Mixture of different font sizes to highlight particular text elements.

```html
<!DOCTYPE html>
<html lang="en">
<head>
<meta charset="utf-8">
<title>Q7 Engineering – Rail Sector Brochure</title>
<link rel="stylesheet" href="https://fonts.googleapis.com/css2?family=Cabin:wght@400;500;600&display=swap">
<style>
:root{
  --page-bg:#e4e4e4;
  --blue:#1f6fb5;
  --blue-deep:#0c4c8a;
  --blue-light:#3b93d6;
  --charcoal:#45484d;
  --charcoal-deep:#2f3236;
  --white:#ffffff;
  --ink:#3a3d42;
  --photo-light:#c9cbcd;
  --photo-mid:#8d9094;
  --photo-dark:#3c3f43;
}
*{box-sizing:border-box;margin:0;padding:0}
html,body{width:1200px;height:2400px;overflow:hidden}
body{background:var(--page-bg);font-family:"Cabin",sans-serif;color:var(--ink);position:relative}
.spread{position:absolute;left:50px;width:1100px;height:778px;display:flex;box-shadow:0 10px 30px rgba(0,0,0,.18);background:var(--white)}
.spread--outside{top:372px}
.spread--inside{top:1250px}
.panel{position:relative;width:366.67px;height:100%;overflow:hidden}
.photo{position:absolute;left:0;right:0}
.brand{display:flex;align-items:center;gap:8px;font-weight:600;font-size:26px;color:var(--blue)}
.brand__square{width:16px;height:16px;background:var(--blue)}
.headline{font-weight:500;text-transform:uppercase;letter-spacing:.5px;line-height:1.15}
.tagline{font-size:13px;font-style:normal;opacity:.9}
.body{font-size:10.5px;line-height:1.5}
.url-band{position:absolute;left:0;right:0;height:34px;display:flex;align-items:center;padding-left:30px;font-size:15px;letter-spacing:.3px}

/* outside left: inside flap */
.flap .photo{top:0;height:300px;background:linear-gradient(160deg,var(--photo-light),var(--photo-mid) 60%,var(--photo-dark))}
.flap__heading{position:absolute;top:320px;left:30px;right:30px;color:var(--blue);font-size:19px;font-style:italic;line-height:1.2}
.flap__body{position:absolute;top:395px;left:30px;right:30px}
.flap__body p+p{margin-top:10px}
.flap .url-band{bottom:24px;background:var(--blue);color:var(--white)}

/* outside middle: back */
.back{background:var(--charcoal);color:var(--white);text-align:center}
.back .brand{justify-content:center;margin-top:60px;color:var(--white)}
.back .brand__square{background:var(--blue-light)}
.back__headline{margin-top:26px;font-size:21px}
.back__tagline{margin-top:10px}
.contact{margin-top:34px;font-size:12px;line-height:1.5}
.contact dt{margin-top:14px;font-weight:500}
.back .photo{bottom:0;height:190px;background:linear-gradient(180deg,var(--charcoal),var(--photo-mid) 55%,var(--photo-light))}

/* outside right: cover */
.cover .brand{position:absolute;top:44px;left:70px}
.cover .photo{top:120px;height:420px;background:linear-gradient(135deg,var(--photo-light),var(--photo-mid) 55%,var(--photo-dark))}
.cover__diag{position:absolute;inset:0}
.cover__text{position:absolute;left:30px;right:24px;top:530px;color:var(--white)}
.cover__headline{font-size:24px}
.cover__tagline{margin-top:10px}
.cover .url-band{bottom:38px;background:var(--white);color:var(--charcoal)}

/* inside left */
.capability{background:var(--charcoal-deep);color:var(--white)}
.capability__heading{position:absolute;top:40px;left:28px;right:28px;color:var(--blue-light);font-size:17px;line-height:1.25}
.capability__body{position:absolute;top:100px;left:28px;right:28px}
.capability__body p+p{margin-top:10px}
.capability__list{margin-top:8px;padding-left:14px}
.capability__list li{margin-top:3px}
.capability .photo{bottom:0;height:250px;background:linear-gradient(180deg,var(--charcoal-deep),var(--photo-dark) 40%,var(--photo-mid))}

/* inside middle */
.systems{background:linear-gradient(180deg,var(--blue-light),var(--blue) 45%,var(--blue-deep));color:var(--white)}
.systems__intro{position:absolute;top:36px;left:28px;right:28px}
.system-list{position:absolute;top:150px;left:28px;right:24px;list-style:none}
.system{display:flex;gap:14px;margin-bottom:26px;align-items:flex-start}
.system__icon{flex:0 0 58px;height:58px}
.system__title{font-size:11.5px;font-weight:600;text-transform:uppercase;letter-spacing:.3px}
.system__points{list-style:none;font-size:9.5px;line-height:1.45;margin-top:3px}
.system__points li::before{content:"• "}
.systems .url-band{bottom:30px;justify-content:center;padding-left:0}

/* inside right */
.solutions .headline{position:absolute;top:40px;left:28px;right:28px;color:var(--blue);font-size:21px}
.solutions__body{position:absolute;top:110px;left:28px;right:28px}
.solutions__body p+p{margin-top:10px}
.solutions .photo{bottom:0;height:230px;background:linear-gradient(200deg,var(--photo-light),var(--photo-mid) 60%,var(--photo-dark))}
.fold-wave{position:absolute;top:0;left:0;width:100%;height:100%;pointer-events:none}
</style>
</head>
<body>

<section class="spread spread--outside" aria-label="Brochure outside">
  <article class="panel flap">
    <div class="photo" role="img" aria-label="Black and white photo of converging railway tracks"></div>
    <h2 class="flap__heading">A trusted provider to the world's most exacting customers</h2>
    <div class="flap__body body">
      <p>Q7 Engineering is an Australian engineering consultancy and specialty services organisation for Defence, Maritime and ICT clients. Our Engineering Technical Services are now available to the Rail sector.</p>
      <p>The Engineering Technical Service provides technical resources, guidance and expertise to operators and suppliers across the whole life of a system, from concept and design through integration, testing and support.</p>
    </div>
    <div class="url-band">www.q7engineering.com.au</div>
  </article>

  <article class="panel back">
    <div class="brand"><span class="brand__square"></span>Q7 Engineering</div>
    <h2 class="headline back__headline">Smart solutions that<br>deliver excellence.</h2>
    <p class="tagline back__tagline">We deliver solutions to critical challenges</p>
    <dl class="contact">
      <dt>Main Office Address:</dt>
      <dd>Level 6, 48 Carden Lane<br>Harwick 3990</dd>
      <dt>Career Opportunities:</dt>
      <dd>jobs@q7engineering.com.au</dd>
      <dt>General Enquiries:</dt>
      <dd>info@q7engineering.com.au</dd>
    </dl>
    <div class="photo" role="img" aria-label="Photo of a train in motion with light streaks"></div>
  </article>

  <article class="panel cover">
    <div class="brand"><span class="brand__square"></span>Q7 Engineering</div>
    <div class="photo" role="img" aria-label="Black and white photo of a commuter train at a city platform"></div>
    <svg class="cover__diag" viewBox="0 0 367 778" preserveAspectRatio="none" aria-hidden="true">
      <polygon points="367,200 367,778 0,778 0,500" fill="var(--blue)"/>
      <polygon points="367,260 367,778 120,778" fill="var(--blue-deep)" opacity=".45"/>
    </svg>
    <div class="cover__text">
      <h1 class="headline cover__headline">Smart solutions that<br>deliver excellence.</h1>
      <p class="tagline cover__tagline">We deliver solutions to critical challenges</p>
    </div>
    <div class="url-band">www.q7engineering.com.au</div>
  </article>
</section>

<section class="spread spread--inside" aria-label="Brochure inside">
  <article class="panel capability">
    <h2 class="capability__heading">Q7 Engineering offers insight and ingenuity to solve critical challenges</h2>
    <div class="capability__body body">
      <p>Q7 Engineering is an Australian consulting and engineering firm specialising in Command and Control, Communications and Computer (C4) technologies for customers within industry, Defence and Government Departments.</p>
      <p>Q7 Engineering provides engineering resources, specialty services and project delivery from concept to completion in areas including:</p>
      <ul class="capability__list">
        <li>Command and Control (C2) system integration</li>
        <li>Plain and Secure voice &amp; data TCP/IP communications</li>
        <li>Acoustics, Shock and Vibration design, analysis and test</li>
        <li>RF System Visualisation, Modelling and Analytics</li>
        <li>Networked systems including VoIP, IPTV, CCTV and Videowall technologies</li>
        <li>Logistics, Training and ongoing program support solutions</li>
      </ul>
    </div>
    <div class="photo" role="img" aria-label="Photo of an operator at a rail control centre with monitor wall"></div>
  </article>

  <article class="panel systems">
    <p class="systems__intro body">Q7 Engineering staff have been at the forefront of major program delivery to address unique technical challenges for decades. Our staff are leaders in their field and possess in-depth knowledge of systematic approaches to the most complex problems.</p>
    <ul class="system-list">
      <li class="system">
        <svg class="system__icon" viewBox="0 0 58 58" aria-hidden="true"><circle cx="29" cy="29" r="28" fill="var(--white)"/><rect x="16" y="18" width="26" height="17" rx="2" fill="none" stroke="var(--blue)" stroke-width="2.5"/><path d="M24 41h10M29 35v6" stroke="var(--blue)" stroke-width="2.5"/></svg>
        <div><h3 class="system__title">Network Systems – 40%</h3>
          <ul class="system__points"><li>Converged network design</li><li>Carrier grade backbone links</li><li>Secure data and voice transport</li></ul></div>
      </li>
      <li class="system">
        <svg class="system__icon" viewBox="0 0 58 58" aria-hidden="true"><circle cx="29" cy="29" r="28" fill="var(--white)"/><path d="M29 44V26M22 20a10 10 0 0 1 14 0M18 15a16 16 0 0 1 22 0" fill="none" stroke="var(--blue)" stroke-width="2.5" stroke-linecap="round"/><circle cx="29" cy="25" r="3" fill="var(--blue)"/></svg>
        <div><h3 class="system__title">Communications Systems – 35%</h3>
          <ul class="system__points"><li>Train radio and voice systems</li><li>Antenna and RF coverage design</li><li>Passenger information systems</li></ul></div>
      </li>
      <li class="system">
        <svg class="system__icon" viewBox="0 0 58 58" aria-hidden="true"><circle cx="29" cy="29" r="28" fill="var(--white)"/><circle cx="29" cy="23" r="7" fill="none" stroke="var(--blue)" stroke-width="2.5"/><path d="M16 44a13 11 0 0 1 26 0" fill="none" stroke="var(--blue)" stroke-width="2.5"/></svg>
        <div><h3 class="system__title">Command &amp; Control Systems – 20%</h3>
          <ul class="system__points"><li>Control centre integration</li><li>Operator console design</li><li>C2 systems integration</li></ul></div>
      </li>
      <li class="system">
        <svg class="system__icon" viewBox="0 0 58 58" aria-hidden="true"><circle cx="29" cy="29" r="28" fill="var(--white)"/><circle cx="29" cy="29" r="4" fill="var(--blue)"/><circle cx="29" cy="29" r="10" fill="none" stroke="var(--blue)" stroke-width="2.5"/><circle cx="29" cy="29" r="16" fill="none" stroke="var(--blue)" stroke-width="2" opacity=".6"/></svg>
        <div><h3 class="system__title">Sensor Systems – 5%</h3>
          <ul class="system__points"><li>Condition monitoring</li><li>Data logging and analysis</li><li>Shock, vibration and acoustic testing</li></ul></div>
      </li>
    </ul>
    <div class="url-band">www.q7engineering.com.au</div>
  </article>

  <article class="panel solutions">
    <h2 class="headline">Smart solutions that<br>deliver excellence.</h2>
    <div class="solutions__body body">
      <p>At Q7 Engineering we have a broad mix of capabilities including abilities in the areas of networking, communications, C2 system integration, sensor and communications systems.</p>
      <p>Our staff have supported the largest telecommunications networks in Australia and aided Defence in building real-time, secure data networks for communications and data sharing.</p>
      <p>We have enabled communications across multiple platforms including aircraft, rail, ships and vehicle platforms that operate reliably under extreme environmental conditions.</p>
      <p>At Q7 Engineering, we are committed to delivering value to all our customers and end users in a manner that inspires.</p>
    </div>
    <div class="photo" role="img" aria-label="Photo of a train crossing a bridge beside a city skyline"></div>
  </article>
</section>

</body>
</html>
```